Product Setup Instructional Infographic/flyer

Converting product instructions into an infographic. Would prefer that the instructions fit on a 4x6 card, front and back, but a slightly larger size is acceptable as well.

Logo Text

Ridgeline Cask (Rebranding just as Ridgeline Cask, instead of Ridgeline Cask Barrels)

Font styles to use
Decorative

Colors

Designer to choose colors to be used in the design.

Requirements
Must have
• NA
Nice to have
• NA
Should not have
• NA

```html
<!DOCTYPE html>
<html lang="en">
<head>
<meta charset="utf-8">
<title>How to Cure the Oak Barrel</title>
<link rel="stylesheet" href="https://fonts.googleapis.com/css2?family=Sancreek&family=Open+Sans:wght@400;600&display=swap">
<style>
  :root {
    --ink: #231f20;
    --title-brown: #3b1a12;
    --green: #7cc242;
    --number: #1f3a14;
    --panel: rgba(74, 50, 40, 0.82);
    --panel-text: #ffffff;
    --tip-green: #8fd14f;
    --wood-faint: #e6ddd3;
    --bottle-faint: #dcdcd6;
    --leaf-faint: #e9f0dc;
    --water: #4fc3ef;
    --barrel-red: #8e3a22;
    --clock: #3a1010;
  }
  html, body { margin: 0; padding: 0; overflow: hidden; }
  body { width: 1200px; height: 1200px; background: #ffffff; }
  .canvas {
    position: relative; width: 1200px; height: 1200px; overflow: hidden;
    font-family: "Open Sans", Arial, sans-serif; color: var(--ink);
  }
  .backdrop { position: absolute; inset: 0; }
  .title {
    position: absolute; left: 0; top: 50px; width: 1200px; margin: 0;
    text-align: center; font-family: "Sancreek", serif; font-weight: 400;
    font-size: 72px; letter-spacing: 2px; color: var(--title-brown); line-height: 1;
  }
  .step-copy {
    position: absolute; margin: 0; font-size: 19px; line-height: 25.5px;
    text-align: justify; text-align-last: left;
  }
  .label { position: absolute; font-size: 19px; line-height: 28px; }
  .art { position: absolute; border-radius: 10px; }
  .tip-panel {
    position: absolute; left: 382px; top: 734px; width: 422px; height: 162px;
    background: var(--panel); border-radius: 10px; padding: 8px 8px 0 7px;
    box-sizing: border-box; color: var(--panel-text);
  }
  .tip-panel .lead { margin: 0; font-size: 19px; line-height: 25px; }
  .tip-panel .tip-head { margin: 0; font-size: 19px; line-height: 25px; color: var(--tip-green); }
  .tip-panel .tip-body { margin: 0; font-size: 13.6px; line-height: 19px; text-align: justify; }
  .connectors { position: absolute; inset: 0; pointer-events: none; }
  .num { font-family: "Open Sans", Arial, sans-serif; font-weight: 600; font-size: 50px; fill: var(--number); }
</style>
</head>
<body>
<div class="canvas">

  <svg class="backdrop" width="1200" height="1200" viewBox="0 0 1200 1200" role="img" aria-label="Faint background of a wooden barrel head, a wine bottle and grape leaves">
    <circle cx="640" cy="600" r="336" fill="var(--wood-faint)" opacity="0.7"/>
    <rect x="928" y="216" width="104" height="952" rx="40" fill="var(--bottle-faint)" opacity="0.75"/>
    <ellipse cx="140" cy="880" rx="120" ry="160" fill="var(--leaf-faint)"/>
    <ellipse cx="960" cy="200" rx="140" ry="80" fill="var(--leaf-faint)"/>
    <ellipse cx="1080" cy="1100" rx="110" ry="90" fill="var(--leaf-faint)"/>
  </svg>

  <h1 class="title">HOW TO CURE THE OAK BARREL</h1>

  <svg class="connectors" width="1200" height="1200" viewBox="0 0 1200 1200">
    <g stroke="var(--green)" stroke-width="6" fill="none" stroke-linecap="round">
      <line x1="132" y1="532" x2="132" y2="820"/>
      <line x1="408" y1="968" x2="660" y2="968"/>
      <line x1="1032" y1="860" x2="1032" y2="1072"/>
      <line x1="1032" y1="860" x2="1060" y2="860"/>
      <line x1="1032" y1="572" x2="1032" y2="788"/>
      <line x1="1032" y1="572" x2="1060" y2="572"/>
      <line x1="836" y1="358" x2="1032" y2="358"/>
      <line x1="474" y1="358" x2="474" y2="560"/>
      <line x1="702" y1="632" x2="702" y2="712"/>
    </g>
    <g fill="var(--green)">
      <circle cx="132" cy="532" r="14"/><circle cx="132" cy="820" r="14"/>
      <circle cx="408" cy="968" r="14"/>
      <circle cx="1032" cy="1072" r="14"/><circle cx="1032" cy="788" r="14"/>
      <circle cx="1032" cy="358" r="14"/><circle cx="474" cy="358" r="14"/>
      <circle cx="474" cy="540" r="14"/><circle cx="702" cy="632" r="14"/>
    </g>
    <g fill="#ffffff" stroke="var(--green)" stroke-width="8">
      <circle cx="250" cy="218" r="36"/><circle cx="132" cy="872" r="36"/>
      <circle cx="680" cy="968" r="36"/><circle cx="1080" cy="860" r="36"/>
      <circle cx="1080" cy="572" r="36"/><circle cx="816" cy="356" r="36"/>
      <circle cx="474" cy="590" r="36"/>
    </g>
    <g class="num" text-anchor="middle">
      <text x="250" y="236">1</text><text x="132" y="890">2</text>
      <text x="680" y="986">3</text><text x="1080" y="878">4</text>
      <text x="1080" y="590">5</text><text x="816" y="374">6</text>
      <text x="474" y="608">7</text>
    </g>
  </svg>

  <!-- Step 1 -->
  <div class="label" style="left:122px;top:234px;">30 min</div>
  <div class="art" role="img" aria-label="Clock beside a water tub with the spigot soaking" style="left:104px;top:268px;width:240px;height:112px;background:linear-gradient(90deg,var(--clock) 0 38%,var(--water) 38%);"></div>
  <p class="step-copy" style="left:104px;top:392px;width:264px;">Rinse and soak the spigot (wooden faucet) and the plug (or bung) in water for about half an hour.</p>

  <!-- Step 2 -->
  <div class="art" role="img" aria-label="Barrel half-filled with water being shaken" style="left:152px;top:560px;width:240px;height:104px;background:linear-gradient(180deg,#f2f6f8,#7cc8ee);opacity:0.85;"></div>
  <p class="step-copy" style="left:178px;top:690px;width:190px;">While waiting, fill the barrel with water until it is half-full. Use your thumb to plug the holes, give it a good shake to get rid of wood chips and debris that might be trapped inside. Let the water out. You may repeat this process three to five times until you satisfied the barrel is thoroughly clean.</p>

  <!-- Step 3 -->
  <div class="art" role="img" aria-label="Barrel head with the bung being inserted, a hand icon and a crossed-out hammer" style="left:472px;top:984px;width:216px;height:136px;background:linear-gradient(180deg,#f4efe9,var(--barrel-red));opacity:0.85;"></div>
  <p class="step-copy" style="left:698px;top:1020px;width:285px;">Plug the barrel with the spigot. You may tighten it securely with your hand. We advise not to use a hammer as it may crack the wood.</p>

  <!-- Step 4 -->
  <p class="step-copy" style="left:814px;top:766px;width:196px;">Place the barrel in a sink, tub, or any place that is OK to get wet.</p>
  <div class="art" role="img" aria-label="Barrel sitting in a tub of water" style="left:814px;top:858px;width:184px;height:130px;background:linear-gradient(180deg,#9fdcf6,var(--water));"></div>

  <!-- Step 5 -->
  <div class="art" role="img" aria-label="Barrel being filled with hot water through a funnel, water leaking" style="left:992px;top:364px;width:144px;height:152px;background:linear-gradient(180deg,#ffffff,#5ab4e8);"></div>
  <p class="step-copy" style="left:815px;top:402px;width:156px;">Using a funnel, fill the barrel with hot water until it is full. Leave the top hole open. Your barrel might leak, and that’s OK. It is not watertight yet and this process will make the wood expand to seal the gaps.</p>

  <!-- Step 6 -->
  <div class="art" role="img" aria-label="Full barrel with no leaks" style="left:484px;top:200px;width:64px;height:136px;background:linear-gradient(180deg,#2c5e8a 0 14%,#ffffff 14% 20%,#4aa3e0);"></div>
  <p class="step-copy" style="left:561px;top:226px;width:540px;text-align:left;">Leave the barrel this way until no more leakages can be seen. This means the wood has expanded and the gaps are sealed. This can take from 30 minutes to an entire week, depending on the size of the barrel.</p>

  <!-- Step 7 -->
  <div class="label" style="left:600px;top:388px;line-height:28px;">four<br>hours</div>
  <div class="art" role="img" aria-label="Barrel draining, a clock, and an empty barrel air drying" style="left:496px;top:420px;width:268px;height:100px;background:linear-gradient(90deg,#8ccdf0,#ffffff 40%,var(--clock) 40% 55%,#f0f0f0 55%);"></div>
  <p class="step-copy" style="left:534px;top:562px;width:234px;">Drain the barrel and let it air dry for no more than four hours.</p>

  <!-- Finished barrel and tip -->
  <div class="art" role="img" aria-label="Red wooden oak barrel with metal hoops on a stand" style="left:440px;top:672px;width:328px;height:240px;background:linear-gradient(180deg,#b0502e,var(--barrel-red));border-radius:60px;"></div>
  <div class="tip-panel">
    <p class="lead">After 4 hours, it is ready to be filled with any spirits or wine of your choice.</p>
    <p class="tip-head">Additional Tip</p>
    <p class="tip-body">If you plan on aging different kinds of alcohol using the same barrel, you must cure the barrel again (Step 6) for three to five days. This will allow the barrel to absorb enough water and prevent the next batch of alcohol from being contaminated.</p>
  </div>

</div>
</body>
</html>
```